Spinning Wheel: Spin & Win

We are looking to design a large sticker cover for a spinning wheel (please see attached reference)

Wheel diameter: 120 cm (1.2meters)

Divided into 8 sections:
1- Free Meal
2- Tolvik Gift Card
3- Haircut or Blowdry
4- Tolvik Gift Card
5- Merchandise
6- Tolvik Gift Card
7- Meal voucher
8- Tolvik Gift Card

Text in the center:
Buy for 200 AED to Spin & Win!
(Spin & Win should be the most dominant visually)

Font: Something classy and elegant (maybe cursive but easily read)

Colors: Khaki - All shades of brown and dark brown (note: the wheel structure is made of wood that is dark brown)

Feel: Wood and Old Paper
Updates

Target Market(s)

Upper Class

Industry/Entity Type

Graphic Design

Font styles to use
Decorative
Script

Requirements
Should not have
• Flashy colors

```html
<!DOCTYPE html>
<html lang="en">
<head>
<meta charset="UTF-8">
<title>Spin &amp; Win Wheel</title>
<link rel="stylesheet" href="https://fonts.googleapis.com/css2?family=Rye&family=Playfair+Display:wght@700&family=Great+Vibes&display=swap">
<style>
  :root {
    --page: #ffffff;
    --wood-light: #b0703c;
    --wood-mid: #8a4f26;
    --wood-dark: #4e2810;
    --wood-edge: #2e1608;
    --seam: #3a1c0b;
    --label-gold: #f0c032;
    --label-outline: #4a1f08;
    --hub-light: #7a2616;
    --hub-dark: #3a0d07;
    --hub-ring: #2a0b05;
    --cream: #f3e6cb;
  }
  html, body {
    margin: 0;
    padding: 0;
    width: 1200px;
    height: 1200px;
    overflow: hidden;
    background: var(--page);
  }
  .canvas {
    width: 1200px;
    height: 1200px;
    display: block;
  }
  .seam {
    stroke: var(--seam);
    stroke-width: 3;
    opacity: 0.75;
  }
  .prize-label {
    font-family: "Rye", "Georgia", serif;
    fill: var(--label-gold);
    stroke: var(--label-outline);
    stroke-width: 5;
    paint-order: stroke fill;
    stroke-linejoin: round;
    text-anchor: middle;
    dominant-baseline: middle;
    filter: url(#labelShadow);
  }
  .hub-intro {
    font-family: "Playfair Display", "Georgia", serif;
    font-weight: 700;
    font-size: 36px;
    fill: var(--cream);
    text-anchor: middle;
    letter-spacing: 1px;
  }
  .hub-script {
    font-family: "Great Vibes", cursive;
    fill: var(--cream);
    text-anchor: middle;
  }
</style>
</head>
<body>
<svg class="canvas" viewBox="0 0 1200 1200" xmlns="http://www.w3.org/2000/svg">
  <defs>
    <radialGradient id="woodFill" cx="50%" cy="50%" r="50%">
      <stop offset="0%" stop-color="var(--wood-light)"/>
      <stop offset="55%" stop-color="var(--wood-mid)"/>
      <stop offset="88%" stop-color="var(--wood-dark)"/>
      <stop offset="100%" stop-color="var(--wood-edge)"/>
    </radialGradient>
    <radialGradient id="hubFill" cx="45%" cy="40%" r="60%">
      <stop offset="0%" stop-color="var(--hub-light)"/>
      <stop offset="100%" stop-color="var(--hub-dark)"/>
    </radialGradient>
    <filter id="wheelShadow" x="-10%" y="-10%" width="120%" height="120%">
      <feDropShadow dx="0" dy="4" stdDeviation="6" flood-color="#000" flood-opacity="0.45"/>
    </filter>
    <filter id="labelShadow" x="-20%" y="-40%" width="140%" height="180%">
      <feDropShadow dx="2" dy="3" stdDeviation="2" flood-color="#1a0802" flood-opacity="0.7"/>
    </filter>
  </defs>

  <circle class="wheel-face" cx="600" cy="600" r="593" fill="url(#woodFill)" filter="url(#wheelShadow)"
          role="img" aria-label="Dark weathered wood grain surface"/>

  <g class="seams" transform="translate(600 600)">
    <line class="seam" x1="180" y1="0" x2="590" y2="0" transform="rotate(0)"/>
    <line class="seam" x1="180" y1="0" x2="590" y2="0" transform="rotate(45)"/>
    <line class="seam" x1="180" y1="0" x2="590" y2="0" transform="rotate(90)"/>
    <line class="seam" x1="180" y1="0" x2="590" y2="0" transform="rotate(135)"/>
    <line class="seam" x1="180" y1="0" x2="590" y2="0" transform="rotate(180)"/>
    <line class="seam" x1="180" y1="0" x2="590" y2="0" transform="rotate(225)"/>
    <line class="seam" x1="180" y1="0" x2="590" y2="0" transform="rotate(270)"/>
    <line class="seam" x1="180" y1="0" x2="590" y2="0" transform="rotate(315)"/>
  </g>

  <g class="prizes">
    <g class="prize prize-free-meal" transform="translate(600 600) rotate(-113) translate(378 0) rotate(180)">
      <text class="prize-label" font-size="54" x="0" y="0" textLength="320" lengthAdjust="spacingAndGlyphs">FREE MEAL</text>
    </g>
    <g class="prize prize-gift-card" transform="translate(600 600) rotate(-67.5) translate(385 0) rotate(180)">
      <text class="prize-label" font-size="52">
        <tspan x="0" y="-36" textLength="200" lengthAdjust="spacingAndGlyphs">TOLVIK</tspan>
        <tspan x="0" y="36" textLength="290" lengthAdjust="spacingAndGlyphs">GIFT CARD</tspan>
      </text>
    </g>
    <g class="prize prize-haircut" transform="translate(600 600) rotate(-23) translate(372 0) rotate(180)">
      <text class="prize-label" font-size="48">
        <tspan x="0" y="-56" textLength="230" lengthAdjust="spacingAndGlyphs">HAIRCUT</tspan>
        <tspan x="0" y="0">OR</tspan>
        <tspan x="0" y="56" textLength="250" lengthAdjust="spacingAndGlyphs">BLOWDRY</tspan>
      </text>
    </g>
    <g class="prize prize-gift-card" transform="translate(600 600) rotate(22.5) translate(385 0) rotate(180)">
      <text class="prize-label" font-size="52">
        <tspan x="0" y="-36" textLength="200" lengthAdjust="spacingAndGlyphs">TOLVIK</tspan>
        <tspan x="0" y="36" textLength="290" lengthAdjust="spacingAndGlyphs">GIFT CARD</tspan>
      </text>
    </g>
    <g class="prize prize-merchandise" transform="translate(600 600) rotate(68.5) translate(368 0) rotate(180)">
      <text class="prize-label" font-size="54" x="0" y="0" textLength="360" lengthAdjust="spacingAndGlyphs">MERCHANDISE</text>
    </g>
    <g class="prize prize-gift-card" transform="translate(600 600) rotate(112.5) translate(385 0) rotate(180)">
      <text class="prize-label" font-size="52">
        <tspan x="0" y="-36" textLength="200" lengthAdjust="spacingAndGlyphs">TOLVIK</tspan>
        <tspan x="0" y="36" textLength="290" lengthAdjust="spacingAndGlyphs">GIFT CARD</tspan>
      </text>
    </g>
    <g class="prize prize-meal-voucher" transform="translate(600 600) rotate(156) translate(368 0) rotate(180)">
      <text class="prize-label" font-size="52">
        <tspan x="0" y="-36" textLength="150" lengthAdjust="spacingAndGlyphs">MEAL</tspan>
        <tspan x="0" y="36" textLength="260" lengthAdjust="spacingAndGlyphs">VOUCHER</tspan>
      </text>
    </g>
    <g class="prize prize-gift-card" transform="translate(600 600) rotate(202.5) translate(385 0) rotate(180)">
      <text class="prize-label" font-size="52">
        <tspan x="0" y="-36" textLength="200" lengthAdjust="spacingAndGlyphs">TOLVIK</tspan>
        <tspan x="0" y="36" textLength="290" lengthAdjust="spacingAndGlyphs">GIFT CARD</tspan>
      </text>
    </g>
  </g>

  <g class="hub">
    <circle cx="600" cy="600" r="186" fill="var(--hub-ring)" filter="url(#wheelShadow)"/>
    <circle cx="600" cy="600" r="178" fill="url(#hubFill)"/>
    <text class="hub-intro" x="600" y="480">BUY FOR</text>
    <text class="hub-intro" x="600" y="522">200 AED TO</text>
    <text class="hub-script" x="575" y="628" font-size="112">Spin</text>
    <text class="hub-script" x="695" y="668" font-size="92">&amp;</text>
    <text class="hub-script" x="590" y="738" font-size="104">Win!</text>
  </g>
</svg>
</body>
</html>
```